Web Design for Real Estate Lending business

I need a web design for my real estate private lending business. The name of the business is Halvern Capital Group. I plan on using Wordpress because that platform is the most optimized for SEO, and we will rely heavily on SEO after the website is built.

I want the website to be responsive of course, and have a fresh, professional, and sleek UI.

The 4 main goals of the website will be:
1. Rank in Google for our relevant key words (Los Angeles real estate hard money lending, real estate financing, fix and flip, private lending, etc)
2. Educate them on what our lending platform is capable of.
3. Capture the contact info (email or phone number) of investors & borrowers who are interested
4. Encourage investors and borrowers to contact us directly

This is an example of a similar business's website: https://www.morvelcapital.example/

Here is my business parter's old website:
https://web.archive.org/web/20180822043430/http://www.dumaleqg.example/

All of the information on that website (2nd link) will apply to our business. You can pull the information from that Dumale QG website and make it look more modern / sleek, similar to the 1st link (but better).

We are not selling anything on the website.

I also attached a business card template. I would like something similar to this but one that looks slightly more corporate / professional. Keep the colors the same though.

```html
<!DOCTYPE html>
<html lang="en">
<head>
<meta charset="utf-8">
<title>Halvern Capital Group</title>
<link rel="stylesheet" href="https://fonts.googleapis.com/css2?family=Montserrat:wght@400;500;600;700&family=Mulish:wght@400;500;600&display=swap">
<style>
:root{
  --blue:#1c4fa3;
  --blue-dark:#163f85;
  --sky:#2f86d6;
  --ink:#2f2f2f;
  --muted:#666666;
  --line:#c9c9c9;
  --paper:#f4f4f4;
  --white:#ffffff;
}
*{box-sizing:border-box;margin:0;padding:0}
html,body{width:1200px;height:4185px;overflow:hidden}
body{position:relative;background:var(--white);font-family:Arial,Helvetica,sans-serif;color:var(--ink)}
.abs{position:absolute}

/* top bar */
.topbar{left:0;top:0;width:1200px;height:57px;background:var(--blue)}
.topbar .call{left:113px;top:19px;color:#fff;font:600 15px 'Montserrat',sans-serif;display:flex;align-items:center;gap:8px}
.topbar .tab{top:10px;height:36px;border:2px solid #fff;color:#fff;font:600 14px 'Montserrat',sans-serif;display:flex;align-items:center;justify-content:center}

/* brand */
.brand{display:flex;align-items:center;gap:12px;font:700 30px/1 'Montserrat',sans-serif;color:var(--blue)}
.brand .mark{width:56px;height:56px;background:var(--blue);flex:none}
.brand span{display:block;line-height:1.08}
.nav{top:120px;left:456px;display:flex;gap:38px;font:500 14px 'Montserrat',sans-serif;color:#222}
.nav .active{color:var(--sky)}

/* hero */
.hero{left:0;top:195px;width:1200px;height:720px;
  background:
    linear-gradient(180deg,rgba(10,20,50,.15),rgba(10,20,50,.35)),
    radial-gradient(ellipse 24% 20% at 52% 48%,rgba(255,205,140,.55),transparent 70%),
    radial-gradient(ellipse 12% 22% at 16% 52%,rgba(255,190,110,.45),transparent 70%),
    radial-gradient(ellipse 14% 16% at 90% 60%,rgba(255,200,130,.4),transparent 70%),
    radial-gradient(ellipse 60% 18% at 50% 88%,rgba(70,150,200,.55),transparent 70%),
    linear-gradient(180deg,#0e2764 0%,#1c3a86 22%,#7b7f8a 45%,#c9c2b4 58%,#3b4a60 76%,#1a3352 100%)}
.hero-title{left:0;width:1200px;text-align:center;color:#fff;font-family:'Montserrat',sans-serif;font-weight:500;text-shadow:0 2px 10px rgba(0,0,0,.35)}
.btn-solid{background:var(--blue);color:#fff;font:600 16px 'Montserrat',sans-serif;display:flex;align-items:center;justify-content:center}
.btn-line{border:3px solid var(--blue);color:var(--blue);font:600 16px 'Montserrat',sans-serif;display:flex;align-items:center;justify-content:center}
.btn-white{border:2px solid #fff;color:#fff;font:600 13px 'Montserrat',sans-serif;display:flex;align-items:center;justify-content:center}

/* welcome */
.welcome{left:0;top:915px;width:1200px;height:695px;background:linear-gradient(180deg,#fff 0%,#eef0f3 100%)}
.photo-team{background:
    radial-gradient(ellipse 22% 26% at 22% 52%,rgba(200,150,95,.75),transparent 70%),
    radial-gradient(ellipse 20% 30% at 50% 60%,rgba(40,55,90,.8),transparent 70%),
    radial-gradient(ellipse 22% 34% at 80% 38%,rgba(35,40,55,.85),transparent 70%),
    linear-gradient(180deg,#e9ebee 0%,#dcdde1 45%,#c4c6cc 70%,#f2f2f2 100%)}
.eyebrow{font:400 30px 'Mulish',sans-serif;color:#333}
.title{font:500 35px 'Mulish',sans-serif;color:var(--blue)}
.copy{font-size:14px;line-height:26px;color:#555;text-align:justify}

/* tiles */
.tile .label{width:100%;text-align:center;color:#fff;text-shadow:0 1px 6px rgba(0,0,0,.5)}
.tile .name{font:500 24px 'Montserrat',sans-serif}
.tile .sub{font:italic 15px Arial,sans-serif;margin-top:10px}
.tile-investors{background:
    radial-gradient(ellipse 40% 20% at 50% 85%,rgba(70,110,40,.9),transparent 70%),
    radial-gradient(ellipse 30% 25% at 50% 45%,rgba(150,140,120,.55),transparent 70%),
    radial-gradient(ellipse 8% 6% at 30% 60%,rgba(255,200,120,.5),transparent 70%),
    linear-gradient(180deg,#3a404c 0%,#2c3532 40%,#2f3b2a 70%,#2d4a22 100%)}
.tile-borrowers{background:
    radial-gradient(ellipse 30% 18% at 85% 10%,rgba(230,140,70,.6),transparent 70%),
    radial-gradient(ellipse 40% 28% at 55% 45%,rgba(225,222,215,.55),transparent 70%),
    radial-gradient(ellipse 12% 22% at 20% 65%,rgba(110,70,45,.8),transparent 70%),
    radial-gradient(ellipse 14% 8% at 35% 38%,rgba(255,200,120,.55),transparent 70%),
    linear-gradient(180deg,#404b5c 0%,#535560 45%,#4a4643 75%,#6e6a66 100%)}

/* lending */
.keys{background:
    radial-gradient(ellipse 30% 30% at 55% 30%,rgba(30,40,70,.95),transparent 70%),
    radial-gradient(ellipse 28% 20% at 35% 48%,rgba(215,170,140,.8),transparent 70%),
    radial-gradient(ellipse 35% 25% at 30% 80%,rgba(245,245,245,.95),transparent 70%),
    radial-gradient(ellipse 20% 30% at 8% 40%,rgba(190,160,120,.6),transparent 70%),
    linear-gradient(120deg,#5a4a3e 0%,#3a3a42 35%,#8a8c92 60%,#e2e2e2 85%,#f2f2f3 100%)}

/* featured */
.section-title{left:0;width:1200px;text-align:center;font:500 36px 'Mulish',sans-serif;color:var(--blue)}
.rule{left:572px;width:56px;height:3px;background:var(--blue)}
.card-img{top:2828px;width:314px;height:220px}
.kitchen{background:
    radial-gradient(ellipse 30% 20% at 45% 62%,rgba(255,255,255,.95),transparent 70%),
    radial-gradient(ellipse 20% 20% at 15% 45%,rgba(110,80,55,.7),transparent 70%),
    radial-gradient(ellipse 40% 12% at 40% 90%,rgba(40,35,30,.6),transparent 70%),
    linear-gradient(180deg,#f2f1ee 0%,#dcd8d0 55%,#a59a8a 100%)}
.fireplace{background:
    radial-gradient(ellipse 12% 12% at 50% 58%,rgba(255,150,60,.85),transparent 70%),
    radial-gradient(ellipse 18% 24% at 50% 55%,rgba(60,55,50,.7),transparent 70%),
    radial-gradient(ellipse 40% 14% at 50% 92%,rgba(170,150,125,.8),transparent 70%),
    linear-gradient(180deg,#f3f2ef 0%,#e4e1db 55%,#b7aa98 100%)}
.lounge{background:
    radial-gradient(ellipse 14% 26% at 80% 30%,rgba(90,120,70,.75),transparent 70%),
    radial-gradient(ellipse 30% 14% at 40% 68%,rgba(150,145,140,.75),transparent 70%),
    radial-gradient(ellipse 20% 12% at 55% 85%,rgba(190,150,100,.7),transparent 70%),
    linear-gradient(180deg,#f4f3ee 0%,#e7e2d6 55%,#c9bca6 100%)}
.card-cap{top:3048px;height:100px;border-left:4px solid var(--blue);padding-left:24px}
.card-cap h3{font:600 18px 'Montserrat',sans-serif;color:#222;padding-top:22px}
.card-cap p{font-size:12.5px;line-height:24px;color:var(--muted);margin-top:6px;width:262px}

/* contact */
.contact{left:0;top:3200px;width:1200px;height:599px;background:var(--paper)}
.field{font-size:13px;color:#333;border-bottom:1px solid var(--line);height:40px;padding-top:4px}
.check{display:flex;align-items:center;gap:12px;font-size:13px;color:#555}
.check i{width:16px;height:16px;border:1px solid #999;background:#fff;display:block}

/* footer */
.footer{left:0;top:3799px;width:1200px;height:386px;background:var(--blue)}
.footer-brand{color:#fff}
.footer-brand .mark{background:#fff}
.finfo{color:#fff}
.finfo h4{font:500 17px 'Montserrat',sans-serif}
.finfo p{font:500 13px/22px 'Montserrat',sans-serif}
.social{top:3952px;width:40px;height:40px;border:2px solid #fff;border-radius:50%;background:rgba(255,255,255,.18)}
.fnav{top:4088px;left:0;width:1200px;display:flex;justify-content:center;gap:38px;font:500 13px 'Montserrat',sans-serif;color:#fff}
.copyright{top:4134px;left:0;width:1200px;text-align:center;font:400 14px 'Montserrat',sans-serif;color:#fff}
</style>
</head>
<body>

<div class="abs topbar">
  <div class="abs call">
    <svg width="14" height="14" viewBox="0 0 24 24"><path fill="#fff" d="M6.6 10.8c1.4 2.8 3.8 5.1 6.6 6.6l2.2-2.2c.3-.3.7-.4 1-.2 1.1.4 2.3.6 3.6.6.6 0 1 .4 1 1V20c0 .6-.4 1-1 1C10.6 21 3 13.4 3 4c0-.6.4-1 1-1h3.5c.6 0 1 .4 1 1 0 1.3.2 2.5.6 3.6.1.3 0 .7-.2 1z"/></svg>
    CALL US : 000.555.0142
  </div>
  <div class="abs tab" style="left:897px;width:99px">INVEST</div>
  <div class="abs tab" style="left:1000px;width:88px">BORROW</div>
</div>

<div class="abs brand" style="left:113px;top:91px">
  <div class="mark"></div>
  <div><span>HALVERN</span><span>CAPITAL GROUP</span></div>
</div>
<nav class="abs nav">
  <span class="active">HOME</span><span>WHO WE ARE</span><span>FEATURED</span><span>RESOURCES</span><span>CAREERS</span><span>CONTACT US</span>
</nav>

<section class="abs hero" role="img" aria-label="Modern white luxury house lit at dusk with a reflecting pool"></section>
<div class="abs hero-title" style="top:476px;font-size:62px;line-height:1">HALVERN</div>
<div class="abs hero-title" style="top:552px;font-size:78px;line-height:1">CAPITAL GROUP</div>
<div class="abs btn-solid" style="left:520px;top:659px;width:160px;height:54px">LEARN MORE</div>

<section class="abs welcome"></section>
<div class="abs photo-team" style="left:113px;top:985px;width:420px;height:492px" role="img" aria-label="Three colleagues reviewing documents at an office desk"></div>
<div class="abs" style="left:336px;top:1276px;width:281px;height:267px;background:var(--blue)"></div>
<div class="abs eyebrow" style="left:681px;top:1030px">Welcome to</div>
<div class="abs title" style="left:681px;top:1068px">Halvern Capital Group</div>
<p class="abs copy" style="left:681px;top:1141px;width:394px">Sed ut perspiciatis unde omnis iste natus error sit voluptatem accusantium doloremque laudantium, totam rem aperiam, eaque ipsa quae ab illo inventore veritatis et quasi architecto beatae vitae dicta sunt explicabo. Nemo enim voluptatem quia voluptas sit aspernatur aut odit aut fugit, sed quia consequuntur magni dolores eos qui ratione voluptatem sequi nesciunt. Neque porro quisquam est, qui dolorem ipsum quia dolor sit amet, consectetur....</p>
<div class="abs btn-line" style="left:681px;top:1374px;width:158px;height:50px">LEARN MORE</div>

<div class="abs tile tile-investors" style="left:0;top:1616px;width:593px;height:488px" role="img" aria-label="Craftsman style family house with lawn at dusk">
  <div class="abs label" style="top:216px"><div class="name">INVESTORS</div><div class="sub">Sed ut perspiciatis unde omnis iste natus</div></div>
  <div class="abs btn-white" style="left:233px;top:296px;width:126px;height:42px">LEARN MORE</div>
</div>
<div class="abs tile tile-borrowers" style="left:607px;top:1616px;width:593px;height:488px" role="img" aria-label="Modern white house with wood cladding at sunset">
  <div class="abs label" style="top:216px"><div class="name">BORROWERS</div><div class="sub">Sed ut perspiciatis unde omnis iste natus</div></div>
  <div class="abs btn-white" style="left:233px;top:296px;width:126px;height:42px">LEARN MORE</div>
</div>

<div class="abs" style="left:0;top:2135px;width:1200px;height:538px;background:#f2f2f3"></div>
<div class="abs keys" style="left:0;top:2135px;width:667px;height:538px" role="img" aria-label="Hand passing house keys over a signed contract"></div>
<div class="abs eyebrow" style="left:704px;top:2277px">Real Estate</div>
<div class="abs title" style="left:704px;top:2320px">Private Lending Business</div>
<p class="abs copy" style="left:706px;top:2382px;width:390px;text-align:left">Nemo enim ipsam voluptatem quia voluptas sit aspernatur aut odit aut fugit, sed quia consequuntur magni dolores eos qui rat ione voluptatem sequi nesciunt.</p>
<div class="abs btn-solid" style="left:708px;top:2481px;width:138px;height:48px">LEARN MORE</div>

<h2 class="abs section-title" style="top:2730px">Featured Investments</h2>
<div class="abs rule" style="top:2793px"></div>
<div class="abs card-img kitchen" style="left:113px" role="img" aria-label="Bright kitchen with island and bar stools"></div>
<div class="abs card-img fireplace" style="left:443px" role="img" aria-label="Living room with fireplace and built-in shelves"></div>
<div class="abs card-img lounge" style="left:775px" role="img" aria-label="Sunny living room with sofa and plants"></div>
<div class="abs card-cap" style="left:137px"><h3>Sed ut perspiciatis unde</h3><p>Nemo enim ipsam voluptatem quia volupt as sit aspernatur aut odit au</p></div>
<div class="abs card-cap" style="left:468px"><h3>Sed ut perspiciatis unde</h3><p>Nemo enim ipsam voluptatem quia volupt as sit aspernatur aut odit au</p></div>
<div class="abs card-cap" style="left:799px"><h3>Sed ut perspiciatis unde</h3><p>Nemo enim ipsam voluptatem quia volupt as sit aspernatur aut odit au</p></div>

<section class="abs contact"></section>
<h2 class="abs section-title" style="top:3245px">Contact Us</h2>
<div class="abs rule" style="top:3306px"></div>
<div class="abs field" style="left:299px;top:3346px;width:269px">First Name</div>
<div class="abs field" style="left:634px;top:3346px;width:271px">Last Name</div>
<div class="abs field" style="left:299px;top:3421px;width:269px">Email</div>
<div class="abs field" style="left:634px;top:3421px;width:271px">Phone</div>
<div class="abs field" style="left:299px;top:3526px;width:606px">Message</div>
<div class="abs" style="left:0;top:3596px;width:1200px;text-align:center;font-size:13px;color:#555">What information are you most interested in? (Select all that apply)</div>
<div class="abs check" style="left:413px;top:3644px"><i></i>Investor Newsletter</div>
<div class="abs check" style="left:619px;top:3644px"><i></i>Borrower Newsletter</div>
<div class="abs btn-line" style="left:525px;top:3694px;width:150px;height:51px">SUBMIT</div>

<footer class="abs footer"></footer>
<div class="abs brand footer-brand" style="left:128px;top:3895px">
  <div class="mark"></div>
  <div><span>HALVERN</span><span>CAPITAL GROUP</span></div>
</div>
<div class="abs" style="left:445px;top:3862px;width:1px;height:120px;background:rgba(255,255,255,.35)"></div>
<div class="abs" style="left:775px;top:3862px;width:1px;height:120px;background:rgba(255,255,255,.35)"></div>
<svg class="abs" style="left:490px;top:3868px" width="18" height="24" viewBox="0 0 18 24"><path d="M9 1a7.5 7.5 0 0 0-7.5 7.5C1.5 14 9 23 9 23s7.5-9 7.5-14.5A7.5 7.5 0 0 0 9 1z" fill="none" stroke="#fff" stroke-width="1.6"/><circle cx="9" cy="8.5" r="2.6" fill="none" stroke="#fff" stroke-width="1.6"/></svg>
<div class="abs finfo" style="left:531px;top:3868px"><h4>Address</h4><p>P.O. Box 512 Lorem Ipsum<br>Dummy MA 02400</p></div>
<div class="abs social" style="left:531px" role="img" aria-label="Professional network profile link"></div>
<div class="abs social" style="left:583px" role="img" aria-label="Social page link"></div>
<svg class="abs" style="left:828px;top:3872px" width="20" height="20" viewBox="0 0 24 24"><path fill="none" stroke="#fff" stroke-width="1.6" d="M6.6 10.8c1.4 2.8 3.8 5.1 6.6 6.6l2.2-2.2c.3-.3.7-.4 1-.2 1.1.4 2.3.6 3.6.6.6 0 1 .4 1 1V20c0 .6-.4 1-1 1C10.6 21 3 13.4 3 4c0-.6.4-1 1-1h3.5c.6 0 1 .4 1 1 0 1.3.2 2.5.6 3.6.1.3 0 .7-.2 1z"/></svg>
<div class="abs finfo" style="left:868px;top:3868px"><h4>Phone</h4><p>000.555.0142</p></div>
<svg class="abs" style="left:828px;top:3942px" width="22" height="16" viewBox="0 0 22 16"><rect x="1" y="1" width="20" height="14" fill="none" stroke="#fff" stroke-width="1.6"/><path d="M1 1l10 8 10-8" fill="none" stroke="#fff" stroke-width="1.6"/></svg>
<div class="abs finfo" style="left:868px;top:3936px"><h4>Email</h4><p>info@halverncapital.example</p></div>
<nav class="abs fnav"><span>HOME</span><span>WHO WE ARE</span><span>FEATURED</span><span>RESOURCES</span><span>CAREERS</span><span>CONTACT US</span></nav>
<div class="abs copyright">Halvern Capital Group © 2021.All Rights Reserved.</div>

</body>
</html>
```